Business Card

To design a professional business card for myself a Beauty Therapist. I will be selling Sol Varenne tanning and other products from home (a beauty room). I have uploaded a file of there promo and I really love their colours. I'm looking for a classey feel to the design, simple but effective. I require my name Tessa Marlowe Beauty Therapist, Mobile- 0413952817, Email - tessa.marlowe@qelmail.com, Facebook - /tessamarlowebeauty & instagram - tessamarlowebeautytherapist . I would like the logo for facebook and instagram. I will also need a A5 & A4 flyer. text futura book to be used.

```html
<!DOCTYPE html>
<html lang="en">
<head>
<meta charset="utf-8">
<title>Tessa Marlowe – Beauty Therapist Business Card</title>
<link href="https://fonts.googleapis.com/css2?family=Jost:wght@300;400&display=swap" rel="stylesheet">
<style>
  :root {
    --card-blue: #52c6df;
    --shade-blue: rgba(38, 140, 190, 0.38);
    --ink-white: #ffffff;
    --page: #ffffff;
  }
  html, body {
    margin: 0;
    padding: 0;
    width: 1200px;
    height: 1000px;
    overflow: hidden;
    background: var(--page);
    font-family: "Jost", "Futura", sans-serif;
    color: var(--ink-white);
  }
  .sheet {
    position: relative;
    width: 1200px;
    height: 1000px;
  }
  .card {
    position: absolute;
    left: 194px;
    width: 812px;
    height: 475px;
    background: var(--card-blue);
    overflow: hidden;
  }
  .card--back { top: 15px; }
  .card--front { top: 503px; }

  .shade {
    position: absolute;
    left: 0;
    width: 100%;
  }
  .card--back .shade--lower {
    top: 195px;
    height: 280px;
    background: radial-gradient(ellipse 48% 100% at 50% 0, var(--shade-blue), transparent 75%);
  }
  .card--front .shade--upper {
    top: 0;
    height: 154px;
    background: radial-gradient(ellipse 48% 100% at 50% 100%, var(--shade-blue), transparent 78%);
  }
  .card--front .shade--lower {
    top: 296px;
    height: 180px;
    background: radial-gradient(ellipse 48% 100% at 50% 0, var(--shade-blue), transparent 78%);
  }

  .identity {
    position: absolute;
    left: 0;
    width: 100%;
    text-align: center;
  }
  .card--back .identity { top: 70px; }
  .card--front .identity { top: 171px; }
  .identity__name {
    margin: 0;
    font-weight: 300;
    font-size: 64px;
    line-height: 76px;
    letter-spacing: 0.5px;
  }
  .identity__role {
    margin: 0;
    font-weight: 300;
    font-size: 26px;
    line-height: 30px;
    letter-spacing: 5.5px;
  }

  .contacts {
    position: absolute;
    left: 158px;
    top: 230px;
    margin: 0;
    padding: 0;
    list-style: none;
  }
  .contacts__item {
    display: flex;
    align-items: center;
    height: 44px;
    font-weight: 300;
    font-size: 31px;
  }
  .contacts__icon {
    width: 40px;
    height: 40px;
    margin-right: 18px;
    flex: none;
  }
</style>
</head>
<body>
<main class="sheet">
  <section class="card card--back" aria-label="Business card, contact side">
    <div class="shade shade--lower"></div>
    <header class="identity">
      <h1 class="identity__name">Tessa Marlowe</h1>
      <p class="identity__role">BEAUTY THERAPIST</p>
    </header>
    <ul class="contacts">
      <li class="contacts__item">
        <svg class="contacts__icon" viewBox="0 0 40 40" aria-hidden="true">
          <circle cx="20" cy="20" r="17.5" fill="none" stroke="#fff" stroke-width="2.5"/>
          <path d="M14 11.5c1-.8 2-.6 2.6.4l1.6 2.8c.5.9.3 1.7-.5 2.3l-1 .7c.8 2.6 2.2 4.9 4 6.6l1.1-.6c.9-.5 1.7-.3 2.3.5l1.8 2.5c.6.9.5 1.8-.4 2.5l-1.3 1c-1.2.9-3 .8-4.4-.3-3.8-3-6.4-7.6-7.2-12.4-.3-1.7.3-3.3 1.4-4z" fill="#fff"/>
        </svg>
        <span>041 395 2817</span>
      </li>
      <li class="contacts__item">
        <svg class="contacts__icon" viewBox="0 0 40 40" aria-hidden="true">
          <circle cx="20" cy="20" r="17.5" fill="none" stroke="#fff" stroke-width="2.5"/>
          <rect x="10.5" y="13.5" width="19" height="13" rx="1" fill="#fff"/>
          <path d="M10.8 14.2 20 21l9.2-6.8" fill="none" stroke="#52c6df" stroke-width="1.6"/>
        </svg>
        <span>tessa.marlowe@qelmail.com</span>
      </li>
      <li class="contacts__item">
        <svg class="contacts__icon" viewBox="0 0 40 40" aria-hidden="true">
          <circle cx="20" cy="20" r="17.5" fill="none" stroke="#fff" stroke-width="2.5"/>
        </svg>
        <span>tessamarlowebeauty</span>
      </li>
      <li class="contacts__item">
        <svg class="contacts__icon" viewBox="0 0 40 40" aria-hidden="true">
          <circle cx="20" cy="20" r="17.5" fill="none" stroke="#fff" stroke-width="2.5"/>
        </svg>
        <span>tessamarlowebeautytherapist</span>
      </li>
    </ul>
  </section>

  <section class="card card--front" aria-label="Business card, name side">
    <div class="shade shade--upper"></div>
    <div class="shade shade--lower"></div>
    <header class="identity">
      <h2 class="identity__name">Tessa Marlowe</h2>
      <p class="identity__role">BEAUTY THERAPIST</p>
    </header>
  </section>
</main>
</body>
</html>
```